Meadowlark Crate Society - New Website Design

Create a professional website for strawberries of the month club; a subscription box business that will INCLUDE dipped strawberries - some with sprinkles. Check out: http://www.plumvine.com for examples. Our website URL will be www.MeadowlarkCrateSociety.com
Please see quillpouch.com; toffeeguild.com and gruffcase.com for the concept I am after. The business has not been launched yet, I am currently in the pre-launch stage using a specialized landing page website, and so the time scale for developing my professional looking website is up to 1-2 weeks.
The webpage should have a fun feel and should match the style of the company logo at toffeeguild.com or gruffcase.com. The pages to include are 'Home', 'About us' and 'Get Started'
Thank you and good luck!

```html
<!DOCTYPE html>
<html lang="en">
<head>
<meta charset="utf-8">
<title>Meadowlark Crate Society – Choose a Plan</title>
<link href="https://fonts.googleapis.com/css2?family=Roboto:wght@400;500;700&family=Chewy&display=swap" rel="stylesheet">
<style>
:root{
  --teal:#6ee3d4;
  --blue:#38b6ed;
  --nav-blue:#1aa6e0;
  --pink:#ff0a6c;
  --ink:#222;
  --muted:#555;
  --line:#e3e3e3;
  --footer-bg:#f4f4f4;
}
*{box-sizing:border-box;margin:0;padding:0}
html,body{width:1200px;height:1164px;overflow:hidden;background:#fff;font-family:'Roboto',sans-serif;color:var(--ink)}
.page{position:relative;width:1200px;height:1164px}
.site-header{position:absolute;left:0;top:0;width:1200px;height:72px;background:#fff;box-shadow:0 2px 6px rgba(0,0,0,.07)}
.brand{position:absolute;display:flex;align-items:center;gap:10px}
.brand-mark{width:38px;height:38px;background:var(--pink);border-radius:4px}
.brand-name{font-size:19px;font-weight:500;color:var(--nav-blue);white-space:nowrap}
.site-header .brand{left:89px;top:17px}
.main-nav{position:absolute;right:88px;top:24px;display:flex;align-items:center;gap:32px;font-size:14px}
.main-nav a{color:var(--nav-blue);text-decoration:none;display:flex;align-items:center;gap:7px}
.main-nav .login{background:var(--pink);color:#fff;padding:0 21px;height:30px;border-radius:15px;font-weight:500;margin-left:-14px}
.breadcrumb{position:absolute;left:87px;top:90px;font-size:13px;color:var(--ink)}
.breadcrumb span{color:var(--nav-blue)}
.section-title{position:absolute;left:0;top:160px;width:1200px;text-align:center;font-family:'Chewy','Roboto',sans-serif;font-size:40px;line-height:48px;color:var(--pink);font-weight:700}
.plan{position:absolute;text-align:center}
.plan-standard{top:260px;width:328px;height:395px;border:1px solid var(--line);background:#fff}
.plan-featured{top:238px;width:328px;height:439px;background:linear-gradient(180deg,#f0eeef 0%,#e6e2e3 55%,#ebe7e8 100%)}
.plan-inner{position:absolute;left:0;width:100%}
.plan-standard .plan-inner{top:44px}
.plan-featured .plan-inner{top:66px}
.plan-name{font-size:15px;color:var(--ink)}
.plan-price{margin-top:3px;font-size:32px;font-weight:700;line-height:38px}
.plan-price small{font-size:19px;font-weight:400;color:var(--muted)}
.plan-note{font-size:11px;letter-spacing:.3px;margin-top:2px}
.plan-photo{width:190px;height:170px;margin:20px auto 0;border-radius:40% 40% 30% 30%}
.photo-dipped{background:radial-gradient(ellipse at 50% 55%,#5a3420 0%,#7a4a2e 45%,#f3efee 75%)}
.photo-trio{width:280px;background:radial-gradient(ellipse at 50% 55%,#b08a6a 0%,#d8cbc2 50%,rgba(240,238,239,0) 75%)}
.photo-cake{background:radial-gradient(ellipse at 50% 50%,#4a2416 0%,#6e3620 45%,#fff 74%)}
.btn{display:inline-block;margin-top:11px;width:138px;height:41px;line-height:41px;border-radius:21px;color:#fff;font-size:12px;font-weight:500;text-decoration:none}
.teal{color:var(--teal)} .blue{color:var(--blue)} .pink{color:var(--pink)}
.bg-teal{background:var(--teal)} .bg-blue{background:var(--blue)} .bg-pink{background:var(--pink)}
.intro{position:absolute;top:730px;left:0;width:1200px;text-align:center;font-size:14px;line-height:21px;color:var(--muted)}
.site-footer{position:absolute;left:0;top:853px;width:1200px;height:311px;background:var(--footer-bg)}
.zigzag{position:absolute;left:0;top:-6px;width:1200px;height:8px}
.site-footer .brand{left:97px;top:72px}
.footer-about{position:absolute;left:97px;top:132px;width:340px;font-size:13px;line-height:22px;color:#444}
.footer-col{position:absolute;top:80px}
.footer-col h3{font-size:17px;font-weight:500;color:#333;margin-bottom:7px}
.footer-col ul{list-style:none}
.footer-col li{font-size:13.5px;line-height:25px;color:#555}
.contact li{display:flex;gap:11px;line-height:16px;margin-bottom:12px}
.contact svg{flex:none;margin-top:2px}
.footer-rule{position:absolute;left:93px;top:266px;width:1000px;height:1px;background:#ddd}
.copyright{position:absolute;left:0;top:283px;width:1193px;text-align:center;font-size:12px;color:#333}
.to-top{position:absolute;left:1112px;top:248px;width:32px;height:32px;border-radius:50%;background:#ff4f7e;display:flex;align-items:center;justify-content:center}
</style>
</head>
<body>
<div class="page">
  <header class="site-header">
    <div class="brand"><span class="brand-mark"></span><span class="brand-name">Meadowlark Crate Society</span></div>
    <nav class="main-nav">
      <a href="#"><svg width="12" height="11" viewBox="0 0 12 11"><path d="M6 0 12 5.5H10.3V11H7.3V7.5H4.7V11H1.7V5.5H0Z" fill="currentColor"/></svg>Home</a>
      <a href="#">About</a>
      <a href="#">Strawberries</a>
      <a href="#">Curation</a>
      <a href="#">Gifting</a>
      <a href="#" class="login">Login</a>
    </nav>
  </header>

  <div class="breadcrumb">Home / <span>Get Started</span></div>

  <h1 class="section-title">Choose a Plan</h1>

  <article class="plan plan-standard" style="left:89px">
    <div class="plan-inner">
      <div class="plan-name">Monthly Plan</div>
      <div class="plan-price teal">$29.99<small>/month</small></div>
      <div class="plan-note">(PLUS SHIPPING)</div>
      <div class="plan-photo photo-dipped" role="img" aria-label="Chocolate-dipped strawberry with drizzle"></div>
      <a href="#" class="btn bg-teal">GET STARTED</a>
    </div>
  </article>

  <article class="plan plan-featured" style="left:436px" role="img" aria-label="Soft blurred backdrop of chocolate treats">
    <div class="plan-inner">
      <div class="plan-name">6 Month Plan</div>
      <div class="plan-price blue">$24.99<small>/month</small></div>
      <div class="plan-note">(PLUS SHIPPING)</div>
      <div class="plan-photo photo-trio" role="img" aria-label="Three dipped strawberries with nuts, stripes and crumbs"></div>
      <a href="#" class="btn bg-blue">GET STARTED</a>
    </div>
  </article>

  <article class="plan plan-standard" style="left:783px">
    <div class="plan-inner">
      <div class="plan-name">12 Month Plan</div>
      <div class="plan-price pink">$21.99<small>/month</small></div>
      <div class="plan-note">(PLUS SHIPPING)</div>
      <div class="plan-photo photo-cake" role="img" aria-label="Chocolate cake topped with a dipped strawberry"></div>
      <a href="#" class="btn bg-pink">GET STARTED</a>
    </div>
  </article>

  <p class="intro">Lorem ipsum dolor sit amet consectetuer adipiscing elit aenean commodo ligula eget dolor.<br>Aenean massa. Cum sociis natoque penatibus et magnis .</p>

  <footer class="site-footer">
    <svg class="zigzag" viewBox="0 0 1200 8" preserveAspectRatio="none">
      <pattern id="zz" width="12" height="8" patternUnits="userSpaceOnUse"><path d="M0 8 6 1 12 8Z" fill="#f4f4f4"/></pattern>
      <rect width="1200" height="8" fill="url(#zz)"/>
    </svg>
    <div class="brand"><span class="brand-mark"></span><span class="brand-name">Meadowlark Crate Society</span></div>
    <p class="footer-about">This is Photoshop's version &nbsp;of Lorem Ipsum. Proin gravida nibh vel velit auctor aliquet. Aenean sollicitudin lorem quis bibendum auctor, nisi elit consequat .</p>

    <div class="footer-col" style="left:506px">
      <h3>Useful Links</h3>
      <ul><li>Home</li><li>About Us</li><li>Get Started</li><li>Contact Us</li></ul>
    </div>
    <div class="footer-col" style="left:700px">
      <h3>Ordering</h3>
      <ul><li>Subscriptions</li><li>Special Occasion Gift Boxes</li><li>My Account</li></ul>
    </div>
    <div class="footer-col contact" style="left:917px">
      <h3>Contact Us</h3>
      <ul>
        <li><svg width="13" height="13" viewBox="0 0 24 24"><path d="M6.6 10.8a15 15 0 0 0 6.6 6.6l2.2-2.2c.3-.3.7-.4 1-.2 1.1.4 2.3.6 3.6.6.6 0 1 .4 1 1V20c0 .6-.4 1-1 1A17 17 0 0 1 3 4c0-.6.4-1 1-1h3.5c.6 0 1 .4 1 1 0 1.3.2 2.5.6 3.6.1.3 0 .7-.2 1z" fill="#1aa6e0"/></svg><span>Phone :<br>555 - 013 2290</span></li>
        <li><svg width="13" height="10" viewBox="0 0 13 10"><rect x=".5" y=".5" width="12" height="9" fill="none" stroke="#1aa6e0"/><path d="M.5.5 6.5 5.5 12.5.5" fill="none" stroke="#1aa6e0"/></svg><span>Email :<br>www.example.com</span></li>
      </ul>
    </div>

    <div class="footer-rule"></div>
    <a href="#" class="to-top" aria-label="Back to top"><svg width="10" height="6" viewBox="0 0 10 6"><path d="M1 5 5 1 9 5" fill="none" stroke="#fff" stroke-width="1.6"/></svg></a>
    <p class="copyright">Cpyright 2017 | All Right Reserved</p>
  </footer>
</div>
</body>
</html>
```